Plumbing and heating business card design

i need a new business card for the company i work for called Dr. Brightpipe. It is a plumbing and heating company that has been operating for over 30 years. We are not like these big plumbing companies that have ways to charge the customer as much as possible. Our company does only what is necessary and what is needed to do the job right the first time without the high cost. we are a neighborhood business which kind of explains why we don't charge customers through the roof. I would like to see a design with a nice background anything but just plain white. maybe like a light blue at the top of the design. on the back of the card i would like it to say " T. Vandermeer's Dr. Brightpipe". maybe add some color to the lettering on the front of the card for example blue font for plumbing and red font for heating. raised print. im sure Cardolux designers will make it look good. The final design should help spread a good word about our company and help grow business.

Industry/Entity Type

Business

Contact Information for Business Card

Dr. Brightpipe, Plumbing & heating, Gordon Tasker, Northeast District Operations manager, 4827 Birchwell st., Office:(555)-284-1937, doctorbrightpipe@mailverra.net

Requirements
Must have
• raised print finish and a nice sturdy feel.

```html
<!DOCTYPE html>
<html lang="en">
<head>
<meta charset="utf-8">
<title>Dr. Brightpipe – Business Card</title>
<link href="https://fonts.googleapis.com/css2?family=Bebas+Neue&family=Open+Sans:ital,wght@0,400;0,700;1,400&family=Roboto+Condensed:wght@400&display=swap" rel="stylesheet">
<style>
  :root {
    --page-bg: #ffffff;
    --card-white: #ffffff;
    --blue-light: #4a8aa8;
    --blue-mid: #2f6a88;
    --blue-deep: #1d4760;
    --navy: #0d2c4f;
    --name-top: #3b86ad;
    --name-bottom: #0f3f60;
    --title-ink: #333a40;
    --contact-ink: #ffffff;
    --sub-ink: #1e5e84;
    --back-top: #2c6b8e;
    --back-bottom: #f2f7fa;
  }
  html, body {
    margin: 0;
    width: 1200px;
    height: 619px;
    overflow: hidden;
    background: var(--page-bg);
  }
  .canvas { position: relative; width: 1200px; height: 619px; }
  .card {
    position: absolute;
    top: 170px;
    width: 500px;
    height: 290px;
    overflow: hidden;
    box-shadow: 0 0 0 1px rgba(0,0,0,0.06);
  }
  .card--front { left: 80px; background: var(--card-white); }
  .card--back {
    left: 640px;
    background: linear-gradient(180deg, var(--back-top) 0%, #3f7f9f 35%, #a9c9d8 72%, var(--back-bottom) 100%);
  }
  .front-art { position: absolute; inset: 0; }
  .holder-name {
    position: absolute;
    left: 38px;
    top: 44px;
    margin: 0;
    font-family: "Bebas Neue", "Oswald", sans-serif;
    font-weight: 400;
    font-size: 46px;
    letter-spacing: 1.5px;
    line-height: 1;
    background: linear-gradient(180deg, var(--name-top), var(--name-bottom));
    -webkit-background-clip: text;
    background-clip: text;
    color: transparent;
  }
  .holder-title {
    position: absolute;
    left: 40px;
    top: 92px;
    margin: 0;
    font-family: "Open Sans", sans-serif;
    font-style: italic;
    font-size: 13px;
    color: var(--title-ink);
  }
  .contact-list {
    position: absolute;
    left: 270px;
    top: 200px;
    margin: 0;
    padding: 0;
    list-style: none;
    font-family: "Open Sans", sans-serif;
    font-size: 12.5px;
    color: var(--contact-ink);
  }
  .contact-list li { display: flex; align-items: center; height: 21px; }
  .contact-icon { width: 12px; height: 12px; margin-right: 9px; fill: var(--contact-ink); }
  .service-line {
    position: absolute;
    left: 0; right: 0;
    top: 72px;
    margin: 0;
    text-align: center;
    font-family: "Open Sans", sans-serif;
    font-weight: 700;
    font-size: 34px;
    color: #ffffff;
    letter-spacing: -0.5px;
    text-shadow: 0 1px 2px rgba(0,0,0,0.25);
  }
  .service-line .amp { font-size: 20px; font-weight: 700; }
  .company-line {
    position: absolute;
    left: 0; right: 0;
    top: 128px;
    display: flex;
    align-items: center;
    justify-content: center;
    gap: 10px;
    margin: 0;
    font-family: "Roboto Condensed", sans-serif;
    font-size: 17px;
    letter-spacing: 0.6px;
    color: var(--sub-ink);
  }
  .company-line::before, .company-line::after {
    content: "";
    width: 34px;
    height: 1px;
    background: rgba(30, 70, 100, 0.5);
  }
</style>
</head>
<body>
<main class="canvas">
  <section class="card card--front" aria-label="Business card front">
    <svg class="front-art" viewBox="0 0 500 290" width="500" height="290" aria-hidden="true">
      <defs>
        <linearGradient id="panelBlue" x1="0" y1="0" x2="1" y2="1">
          <stop offset="0" stop-color="#5a97b3"/>
          <stop offset="0.5" stop-color="#326f8e"/>
          <stop offset="1" stop-color="#1d4760"/>
        </linearGradient>
      </defs>
      <polygon points="500,10 500,290 30,290" fill="url(#panelBlue)"/>
      <polygon points="486,0 500,0 500,10 30,290 12,290" fill="#0d2c4f"/>
    </svg>
    <h1 class="holder-name">Gordon Tasker</h1>
    <p class="holder-title">Northeast District Operations Manager</p>
    <ul class="contact-list">
      <li>
        <svg class="contact-icon" viewBox="0 0 12 12" aria-hidden="true"><path d="M3 0h6a1 1 0 0 1 1 1v10a1 1 0 0 1-1 1H3a1 1 0 0 1-1-1V1a1 1 0 0 1 1-1zm0.5 1.5v8h5v-8z"/></svg>
        (555)-284-1937
      </li>
      <li>
        <svg class="contact-icon" viewBox="0 0 12 12" aria-hidden="true"><path d="M0 2.5h12v1L6 7 0 3.5z M0 5l6 3.5L12 5v5H0z"/></svg>
        doctorbrightpipe@mailverra.net
      </li>
      <li>
        <svg class="contact-icon" viewBox="0 0 12 12" aria-hidden="true"><path d="M6 0a4.2 4.2 0 0 1 4.2 4.2C10.2 7.5 6 12 6 12S1.8 7.5 1.8 4.2A4.2 4.2 0 0 1 6 0zm0 2.4a1.8 1.8 0 1 0 0 3.6 1.8 1.8 0 0 0 0-3.6z"/></svg>
        4827 Birchwell st.
      </li>
    </ul>
  </section>

  <section class="card card--back" aria-label="Business card back">
    <h2 class="service-line">Plumbing <span class="amp">&amp;</span> Heating</h2>
    <p class="company-line">T. VANDERMEER'S DR. BRIGHTPIPE</p>
  </section>
</main>
</body>
</html>
```